QOR Infographic Design and Business Card design

We have an infographic but it could use some updating and creativity applied to it. Would like to match it a bit more to our current logo and web design (although it doesn’t have to match per se, thinking of updating it too) http://qor-advisory.example/QOR_Advisory/QOR_Advisory___Your_treasury_pricing_and_fee_negotiation_specialists.html
Can be double sided

Target Market(s)

Companies that make more than $150MM a year

Industry/Entity Type

Business

Contact Information for Business Card

Uploaded the logo and you can also look at the website.

Font styles to use
Sans Serif

Requirements
Must have
• Must look professional. Looking to stick to the same colors in the logo, the logo won’t change. Very open after that
Nice to have
• Front and back on the card

```html
<!DOCTYPE html>
<html lang="en">
<head>
<meta charset="utf-8">
<title>QOR Advisory – Business Card</title>
<link rel="stylesheet" href="https://fonts.googleapis.com/css2?family=Arimo:wght@400;700&display=swap">
<style>
  :root {
    --bg: #e9e6e1;
    --card: #ffffff;
    --red: #b3141b;
    --red-dark: #8e0d12;
    --grey-text: #6d6d6d;
    --logo-grey: #4a4a4a;
    --white: #ffffff;
  }
  * { box-sizing: border-box; margin: 0; padding: 0; }
  html, body {
    width: 1200px; height: 950px; overflow: hidden;
    background: var(--bg);
    font-family: "Arimo", Arial, sans-serif;
  }
  .canvas { position: relative; width: 1200px; height: 950px; }
  .card {
    position: absolute; width: 640px; height: 366px;
    background: var(--card);
    box-shadow: 0 10px 28px rgba(0,0,0,.22);
    overflow: hidden;
  }
  .card--back { left: 80px; top: 70px; }
  .card--front { left: 480px; top: 505px; }

  .brand { position: absolute; display: flex; flex-direction: column; align-items: flex-start; }
  .brand__name { font-weight: 700; color: var(--logo-grey); letter-spacing: .06em; line-height: 1; }
  .brand__url { font-weight: 700; color: var(--grey-text); }

  .card--back .brand { right: 46px; bottom: 70px; }
  .card--back .brand__name { font-size: 30px; }
  .card--back .brand__url { font-size: 15px; margin-top: 6px; }

  .card--front .brand { left: 190px; top: 38px; }
  .card--front .brand__name { font-size: 46px; }
  .card--front .brand__url { font-size: 21px; margin-top: 8px; }

  .band { position: absolute; inset: 0; width: 100%; height: 100%; }

  .holder {
    position: absolute; left: 34px; bottom: 30px; color: var(--white);
    font-size: 16px; line-height: 1.3;
  }
  .holder__name { font-size: 22px; font-weight: 700; margin-bottom: 2px; }

  .contacts {
    position: absolute; right: 24px; top: 150px; list-style: none;
    color: var(--white); font-size: 16px; line-height: 1.6; text-align: right;
  }
  .contacts li { display: flex; justify-content: flex-end; align-items: center; gap: 8px; }
  .contacts svg { width: 14px; height: 14px; fill: var(--white); }
</style>
</head>
<body>
<main class="canvas">

  <section class="card card--back" aria-label="Card back">
    <div class="brand">
      <span class="brand__name">QOR</span>
      <span class="brand__url">QOR-Advisory.example</span>
    </div>
  </section>

  <section class="card card--front" aria-label="Card front">
    <svg class="band" viewBox="0 0 640 366" preserveAspectRatio="none" aria-hidden="true">
      <defs>
        <linearGradient id="bandFill" x1="0" y1="0" x2="1" y2="1">
          <stop offset="0" stop-color="#b3141b"/>
          <stop offset="1" stop-color="#8e0d12"/>
        </linearGradient>
      </defs>
      <path d="M0,236 C210,205 430,140 640,108 L640,366 L0,366 Z" fill="url(#bandFill)"/>
      <path d="M0,228 C210,197 430,132 640,100" fill="none" stroke="#b3141b" stroke-width="1.5"/>
    </svg>

    <div class="brand">
      <span class="brand__name">QOR</span>
      <span class="brand__url">QOR-Advisory.example</span>
    </div>

    <div class="holder">
      <p class="holder__name">Daniel Reyes</p>
      <p>CEO/Founder</p>
      <p>4120 Larkspur Drive</p>
      <p>Juneau, Alaska 99801</p>
    </div>

    <ul class="contacts">
      <li>555 210 4417
        <svg viewBox="0 0 16 16" aria-label="Phone"><path d="M2 5c0-2 2-3 6-3s6 1 6 3l-3 1-1-2H6L5 6 2 5zm2 2h8l2 6H2z"/></svg></li>
      <li>555 382 6091
        <svg viewBox="0 0 16 16" aria-label="Mobile"><path d="M4 1h8v14H4zm2 2v9h4V3z"/></svg></li>
      <li>555 764 3158
        <svg viewBox="0 0 16 16" aria-label="Fax"><path d="M4 1h7v4H4zM1 6h14v7h-3v2H4v-2H1zm5 5v2h4v-2z"/></svg></li>
      <li>mail@qor-advisory.example
        <svg viewBox="0 0 16 16" aria-label="Email"><path d="M1 3h14v10H1zm1 1v1l6 4 6-4V4z"/></svg></li>
    </ul>
  </section>

</main>
</body>
</html>
```